Business card design needed

I run a life coaching business.
I coach individuals, businesses & groups.
Our aim is create massive change for our clients.
I would like to see a card that is inspirational, something that provokes the thought of achieving your personal best.
Be your own inspiration is a phrase I am considering using.

Target Market(s)

People who are looking to create a massive change in their lives.

Industry/Entity Type

Life Coaching

Contact Information for Business Card

Harbor Light Coaching
Neil Pardoe
Head Coach
email neil@vorunel.com.au
Mob 0412 586 337

Logo styles of interest
Abstract Logo
Requirements
Must have
• I wouldlike to have a free introductory offer on the reverse side of the card.
It would read something like:
Is coaching for me/you?
Try a free 45 minute session.
Book now call or email for your appointment.

```html
<!DOCTYPE html>
<html lang="en">
<head>
<meta charset="utf-8">
<title>Harbor Light Coaching – Business Card</title>
<link rel="stylesheet" href="https://fonts.googleapis.com/css2?family=Fredoka:wght@500;600;700&display=swap">
<style>
  :root {
    --stage: #2a2a2a;
    --ink: #0c0c0c;
    --teal: #17a7bf;
    --teal-deep: #0a7c90;
    --sheen: #e9eef0;
    --soft-white: #e4e8ea;
    --figure: #d6d9db;
  }
  * { margin: 0; padding: 0; box-sizing: border-box; }
  html, body {
    width: 1200px; height: 814px; overflow: hidden;
    background: var(--stage);
    font-family: "Fredoka", sans-serif;
  }
  .stage {
    position: relative; width: 1200px; height: 814px;
    display: flex; justify-content: center; align-items: center; gap: 60px;
  }
  .card {
    position: relative; width: 440px; height: 640px; overflow: hidden;
    background: var(--ink);
    box-shadow: 0 18px 40px rgba(0,0,0,.55);
  }
  .card-wave { position: absolute; inset: 0; width: 100%; height: 100%; }
  .card-content { position: absolute; inset: 0; text-align: center; }

  .hero-figure {
    position: absolute; left: 150px; top: 28px; width: 150px; height: 210px;
    border-radius: 40% 50% 45% 40%;
    background: radial-gradient(ellipse at 50% 40%, var(--figure), rgba(214,217,219,.55));
  }
  .brand-name {
    position: absolute; left: 0; right: 0; top: 262px;
    font-weight: 700; font-size: 46px; line-height: 1.02;
    letter-spacing: 1px; color: var(--ink); text-transform: uppercase;
  }
  .offer {
    position: absolute; left: 0; right: 0; top: 468px;
    font-weight: 600; font-size: 22px; line-height: 1.35; color: var(--soft-white);
  }
  .offer .strong { color: var(--ink); }

  .coach-name {
    position: absolute; left: 0; right: 0; top: 170px;
    font-weight: 700; font-size: 36px; letter-spacing: 1px; line-height: 1; color: var(--ink);
    text-transform: uppercase;
  }
  .coach-role {
    position: absolute; left: 0; right: 0; top: 208px;
    font-weight: 600; font-size: 18px; color: var(--ink);
  }
  .label {
    position: absolute; left: 0; right: 0;
    font-weight: 700; font-size: 19px; letter-spacing: 1px; color: var(--soft-white);
    text-transform: uppercase;
  }
  .label-email { top: 290px; }
  .label-mobile { top: 392px; }
  .contact {
    position: absolute; left: 0; right: 0;
    font-weight: 600; color: var(--ink);
  }
  .contact-email { top: 318px; font-size: 29px; }
  .contact-mobile { top: 420px; font-size: 38px; letter-spacing: 1px; }
</style>
</head>
<body>
<main class="stage">

  <section class="card card-front">
    <svg class="card-wave" viewBox="0 0 440 640" preserveAspectRatio="none" aria-hidden="true">
      <defs>
        <linearGradient id="tealFront" x1="0" y1="0" x2="0" y2="1">
          <stop offset="0" stop-color="#1cb0c8"/>
          <stop offset="1" stop-color="#0a7c90"/>
        </linearGradient>
      </defs>
      <path d="M0 330 C 90 230, 150 180, 260 140 C 340 112, 400 70, 440 20 L440 640 L0 640 Z" fill="#e9eef0"/>
      <path d="M0 352 C 95 250, 160 198, 268 158 C 345 130, 405 88, 440 42 L440 640 L0 640 Z" fill="url(#tealFront)"/>
    </svg>
    <div class="card-content">
      <div class="hero-figure" role="img" aria-label="Light grey silhouette of a sprinting runner"></div>
      <h1 class="brand-name">Harbor<br>Light<br>Coaching</h1>
      <p class="offer">
        Is coaching for me/you?<br>
        <span class="strong">Try a free 45 minute session.</span><br>
        Book now call or email<br>
        for your appointment.
      </p>
    </div>
  </section>

  <section class="card card-back">
    <svg class="card-wave" viewBox="0 0 440 640" preserveAspectRatio="none" aria-hidden="true">
      <defs>
        <linearGradient id="tealBack" x1="0" y1="0" x2="0" y2="1">
          <stop offset="0" stop-color="#18a9c1"/>
          <stop offset="1" stop-color="#0c8aa0"/>
        </linearGradient>
      </defs>
      <path d="M0 248 C 70 160, 160 130, 270 118 C 350 108, 410 80, 440 40 L440 640 L0 640 Z" fill="#e9eef0"/>
      <path d="M0 270 C 75 178, 165 148, 275 136 C 352 126, 412 98, 440 60 L440 640 L0 640 Z" fill="url(#tealBack)"/>
    </svg>
    <div class="card-content">
      <h2 class="coach-name">Neil Pardoe</h2>
      <p class="coach-role">Head Coach</p>
      <p class="label label-email">Email</p>
      <p class="contact contact-email">neil@vorunel.com.au</p>
      <p class="label label-mobile">Mobile No.</p>
      <p class="contact contact-mobile">0412 586 337</p>
    </div>
  </section>

</main>
</body>
</html>
```